Meridian Dash add on sales tool2017

This will be a flyer to leave with our clients we just did work for. We want to entice them to use our other services over the next 30 days with a discount, money off etc. we will write in the special and the expiration date. I want the client to read the description and see a picture of the service they may want done.

Target Market(s)

Repeat clients

Industry/Entity Type

Cleaning Service

Font styles to use
Serif
Sans Serif

Colors
ec1f27
000000
b1b1b1

Requirements
Must have
• Call to action! look high end market, clients show we do 1st class work.
• Don't Waite
Nice to have
• Classy, quality, I'm open to using other pictures that may look better
Should not have
• Look like a typical carpet cleaners special flyer
• Not to look cluttered

```html
<!DOCTYPE html>
<html lang="en">
<head>
<meta charset="UTF-8">
<title>Meridian Dash – Home Cleaning Flyer</title>
<link href="https://fonts.googleapis.com/css2?family=Raleway:wght@400;700;800&family=Roboto:wght@400;700&display=swap" rel="stylesheet">
<style>
  :root {
    --red: #ec1f27;
    --black: #000000;
    --ink: #222222;
    --grey: #b1b1b1;
    --paper: #ffffff;
    --stage: #e6e6e6;
  }
  * { box-sizing: border-box; margin: 0; padding: 0; }
  html, body { width: 1200px; height: 1200px; overflow: hidden; background: var(--stage); }
  .flyer {
    position: absolute; left: 150px; top: 18px;
    width: 900px; height: 1164px;
    background: var(--paper); overflow: hidden;
    font-family: 'Raleway', sans-serif; color: var(--ink);
  }
  .hero-photo {
    position: absolute; left: 0; top: 0; width: 900px; height: 520px;
    background: linear-gradient(120deg, #eceff1 0%, #d9dde0 45%, #c9ced3 70%, #c9a070 100%);
  }
  .hero-machine {
    position: absolute; left: 500px; top: 40px; width: 400px; height: 400px;
    background: radial-gradient(circle at 50% 55%, #7b8894 0%, #9aa4ad 45%, rgba(200,205,210,0) 72%);
  }
  .hero-curve { position: absolute; left: 0; top: 420px; }
  .brand { position: absolute; left: 65px; top: 150px; display: flex; align-items: center; gap: 12px; }
  .brand-dot { width: 22px; height: 22px; border-radius: 50%; background: var(--red); }
  .brand-name { font-weight: 700; font-size: 31px; color: var(--black); letter-spacing: 0.5px; }
  .tagline {
    position: absolute; left: 65px; top: 202px;
    font-size: 11px; letter-spacing: 5.6px; color: var(--ink); font-weight: 400;
  }
  .headline {
    position: absolute; left: 35px; top: 258px;
    border-left: 7px solid var(--red); padding-left: 20px;
    font-size: 47px; line-height: 45px; font-weight: 400; color: var(--ink);
  }
  .headline strong { color: var(--red); font-weight: 800; }
  .service-photo {
    position: absolute; top: 421px; width: 176px; height: 176px; border-radius: 50%;
    border: 7px solid var(--paper);
  }
  .photo-carpet { left: 29px; background: linear-gradient(160deg, #b9a88f, #7a6650); }
  .photo-upholstery { left: 197px; background: linear-gradient(160deg, #e2ddd5, #b8b0a4); }
  .photo-drapery { left: 364px; background: linear-gradient(160deg, #7d6b5c, #3f3a38); }
  .photo-tile { left: 532px; background: linear-gradient(160deg, #b0a89d, #8a8378); }
  .photo-stone { left: 699px; background: linear-gradient(160deg, #d6e7ec, #a5c0c8); }
  .service { position: absolute; top: 608px; width: 168px; }
  .service h2 {
    color: var(--red); font-weight: 800; font-size: 20px; line-height: 24px;
    text-transform: uppercase; margin-bottom: 6px;
  }
  .service p { font-size: 14.5px; line-height: 20.5px; color: #333; }
  .svc-carpet { left: 35px; } .svc-upholstery { left: 208px; } .svc-drapery { left: 380px; }
  .svc-tile { left: 553px; } .svc-stone { left: 726px; width: 150px; }
  .bottom-waves { position: absolute; left: 0; top: 0; }
  .divider { position: absolute; left: 35px; top: 913px; width: 315px; height: 1px; background: var(--grey); }
  .call { position: absolute; left: 35px; top: 930px; display: flex; align-items: center; gap: 12px; }
  .call-icon { width: 60px; height: 60px; }
  .call-label { font-family: 'Roboto', sans-serif; font-size: 20px; color: var(--red); line-height: 22px; }
  .call-label b { font-weight: 700; }
  .call-number { font-family: 'Roboto', sans-serif; font-weight: 700; font-size: 35px; color: var(--red); line-height: 38px; }
  .address {
    position: absolute; right: 66px; top: 898px; text-align: right;
    font-family: 'Roboto', sans-serif; font-size: 18px; line-height: 21px; color: var(--paper);
  }
  .address-icon { position: absolute; right: 40px; top: 900px; width: 22px; height: 22px; }
  .offer {
    position: absolute; left: 537px; top: 955px; width: 327px; height: 172px;
    background: var(--paper); border-radius: 4px;
  }
  .offer-tab { position: absolute; left: 0; top: 0; }
  .offer-title {
    position: absolute; left: 0; top: 4px; width: 327px; text-align: center;
    font-family: 'Roboto', sans-serif; font-weight: 700; font-size: 20px; color: var(--paper); letter-spacing: -0.3px;
  }
  .offer-expires {
    position: absolute; left: 0; bottom: 12px; width: 327px; text-align: center;
    font-size: 14px; color: #777;
  }
</style>
</head>
<body>
<main class="flyer">
  <div class="hero-photo" role="img" aria-label="Photo of a floor scrubbing machine cleaning a light carpet beside a wooden floor">
    <div class="hero-machine"></div>
  </div>
  <svg class="hero-curve" width="900" height="120" viewBox="0 0 900 120">
    <path d="M0 60 C 200 -10, 550 -20, 900 40 L900 120 L0 120 Z" fill="#ffffff"/>
  </svg>

  <div class="brand"><span class="brand-dot"></span><span class="brand-name">MERIDIAN DASH</span></div>
  <div class="tagline">THE ART OF FINE RUG WASHING</div>

  <h1 class="headline">
    <strong>ONE STOP</strong> FOR<br>
    ALL YOUR <strong>HOME</strong><br>
    <strong>CLEANING</strong> NEEDS
  </h1>

  <div class="service-photo photo-carpet" role="img" aria-label="Carpet cleaning wand on a carpet"></div>
  <div class="service-photo photo-upholstery" role="img" aria-label="Upholstery extraction tool on a sofa"></div>
  <div class="service-photo photo-drapery" role="img" aria-label="Technician cleaning drapes"></div>
  <div class="service-photo photo-tile" role="img" aria-label="Tile and grout cleaning tool on a floor"></div>
  <div class="service-photo photo-stone" role="img" aria-label="Polishing machine on a stone floor"></div>

  <section class="service svc-carpet">
    <h2>Carpet<br>Cleaning</h2>
    <p>Don't let dirty carpets spoil the look of your beautiful home!. with 37 years of cleaning carpets experience you can expect your carpets to look like new in most cases.</p>
  </section>
  <section class="service svc-upholstery">
    <h2>Upholstery<br>Cleaning</h2>
    <p>Every day use leaves your sofa's and chairs looking dingy and can smell like dog. Our Dry cleaning ,Shampoo or Rinse extraction will leave the fabric feel like clean sheet!</p>
  </section>
  <section class="service svc-drapery">
    <h2>Drapery<br>Cleaning</h2>
    <p>Drapery's act like a filter attracting atmospheric soil! Making them look dingy, We make it easy to Dry clean in-home! Safe and effective beautiful drapery again.</p>
  </section>
  <section class="service svc-tile">
    <h2>Tile &amp; Grout<br>Cleaning</h2>
    <p>Tile &amp; Grout get neglected! Dirty grout can leave permanent staining. Let our professionals bring back the look of a new floor.</p>
  </section>
  <section class="service svc-stone">
    <h2>Natural Stone Cleaning &amp; Polishing</h2>
    <p>A dull stained Marble - Granite-Travertine and other Natural stone can be revitalized to look NEW again!</p>
  </section>

  <svg class="bottom-waves" width="900" height="1164" viewBox="0 0 900 1164">
    <path d="M0 1060 C 200 1050, 430 960, 600 905 C 700 875, 800 868, 900 868 L900 1164 L0 1164 Z" fill="#ec1f27"/>
    <path d="M420 1000 C 560 925, 700 885, 866 860" stroke="#ec1f27" stroke-width="4" fill="none"/>
    <path d="M0 1000 C 40 1020, 70 1040, 140 1045 C 260 1050, 360 1020, 420 990 C 300 1070, 150 1080, 0 1045 Z" fill="#111111"/>
    <path d="M0 1045 C 140 1080, 300 1070, 420 990 C 330 1080, 200 1110, 0 1080 Z" fill="#ffffff"/>
    <path d="M60 1142 C 250 1160, 450 1110, 560 1060 C 470 1125, 280 1170, 60 1142 Z" fill="#ffffff"/>
  </svg>

  <div class="divider"></div>
  <div class="call">
    <svg class="call-icon" viewBox="0 0 60 60">
      <circle cx="30" cy="30" r="27" fill="none" stroke="#111" stroke-width="3"/>
      <path d="M22 16 l6 8 -4 4 c2 5 5 8 10 10 l4 -4 8 6 -4 6 c-12 0 -24 -12 -24 -24 z" fill="#ec1f27"/>
    </svg>
    <div>
      <div class="call-label"><b>CALL NOW</b> TO BOOK</div>
      <div class="call-number">702 555-0148</div>
    </div>
  </div>

  <div class="address">1475 W. Juniper<br>Dr. Suite B, Las Vegas</div>
  <svg class="address-icon" viewBox="0 0 22 22">
    <circle cx="11" cy="11" r="10" fill="none" stroke="#fff" stroke-width="1.6"/>
    <path d="M5.5 11 L11 6 L16.5 11 M7.5 10 V16 H14.5 V10" fill="none" stroke="#fff" stroke-width="1.6"/>
  </svg>

  <div class="offer">
    <svg class="offer-tab" width="327" height="32" viewBox="0 0 327 32">
      <path d="M20 0 H307 L285 32 H42 Z" fill="#111111"/>
    </svg>
    <div class="offer-title">30 DAY SPECIAL OFFER!</div>
    <div class="offer-expires">Expires XX XX XXXX</div>
  </div>
</main>
</body>
</html>
```